Bright Oak Fitness Facility Business Cards

Business Card Design that incorporates the logo and tagline

Target Market(s)

Fitness, People Who Exercise

Contact Information for Business Card

2817 Mossgrove Bend Road
Tavares, Florida 32190
Phone: 352-555-Jump (5867)
www.brightoakfitness.example
info@brightoakfitness.example

Requirements
Must have
• Logo, Address, Website, email and tagline "More Than A Gym". Colors should be red/black/grey/white

```html
<!DOCTYPE html>
<html lang="en">
<head>
<meta charset="utf-8">
<title>Bright Oak Fitness Facility – Business Card Options</title>
<link rel="stylesheet" href="https://fonts.googleapis.com/css2?family=Barlow:wght@400;600&display=swap">
<style>
  :root {
    --page: #f3f3f3;
    --red: #ee1c24;
    --red-deep: #8a0008;
    --black: #0b0b0b;
    --grey: #8a8a8a;
    --light: #ededed;
    --white: #ffffff;
    --ink: #1a1a1a;
  }
  * { box-sizing: border-box; margin: 0; padding: 0; }
  html, body { width: 1200px; height: 700px; overflow: hidden; }
  body {
    background: var(--page);
    font-family: "Barlow", Arial, sans-serif;
    position: relative;
  }
  .card {
    position: absolute;
    width: 315px;
    height: 180px;
    overflow: hidden;
    border-radius: 7px;
    box-shadow: 0 1px 3px rgba(0,0,0,.12);
  }
  .card-bg { position: absolute; left: 0; top: 0; }
  .brand {
    display: flex; flex-direction: column; align-items: center;
    position: absolute;
  }
  .brand-name {
    font-weight: 600; font-size: 19px; letter-spacing: .3px;
    line-height: 1; white-space: nowrap;
  }
  .brand-name--red { color: var(--red); }
  .brand-name--white { color: var(--white); }
  .brand-mark {
    width: 10px; height: 10px; border-radius: 50%;
    margin-bottom: 7px;
  }
  .tagline { font-size: 10.5px; font-weight: 400; margin-top: 8px; }
  .contact {
    position: absolute;
    font-size: 10px; line-height: 17.5px;
    list-style: none;
    white-space: nowrap;
  }
  .contact--light { color: var(--white); }
  .contact--dark { color: var(--ink); }

  /* Card A – split white and grey */
  .card-split { left: 241px; top: 74px; background: var(--white); }
  .card-split .panel { position: absolute; left: 151px; top: 0; width: 164px; height: 180px; background: var(--grey); }
  .card-split .brand { left: 0; width: 151px; top: 60px; }
  .card-split .contact { left: 171px; top: 50px; }

  /* Card B – grey with black diagonal */
  .card-slant { left: 651px; top: 76px; background: var(--light); border-radius: 0; }
  .card-slant .brand { left: 0; width: 125px; top: 64px; }
  .card-slant .contact { left: 175px; top: 46px; }

  /* Card C – white with red and black bars */
  .card-bars { left: 242px; top: 302px; background: linear-gradient(90deg, #ececec 0%, #ffffff 55%, #f6f6f6 100%); }
  .card-bars .contact { left: 20px; top: 36px; }
  .card-bars .contact li { display: flex; align-items: center; gap: 7px; height: 17.5px; }
  .card-bars .icon { width: 8px; height: 8px; fill: var(--red); flex: none; }
  .card-bars .gap { height: 14px; }
  .card-bars .brand { left: 180px; width: 125px; top: 62px; }
  .card-bars .bar-tagline {
    position: absolute; right: 15px; bottom: 3px;
    color: var(--white); font-size: 10px; font-weight: 600;
  }

  /* Card D – red header */
  .card-header { left: 651px; top: 299px; border-radius: 0;
    background: linear-gradient(180deg, var(--red) 0%, #d50611 55%, var(--red-deep) 100%); }
  .card-header .top { position: absolute; left: 0; top: 0; width: 100%; height: 80px; background: #ff0a14; }
  .card-header .band {
    position: absolute; left: 0; top: 80px; width: 100%; height: 27px;
    background: var(--black); color: var(--white);
    font-size: 11px; font-weight: 600; text-align: center; line-height: 27px;
  }
  .card-header .brand { left: 0; width: 100%; top: 20px; }
  .card-header .contact { left: 23px; top: 114px; line-height: 21px; }
  .card-header .contact span + span { margin-left: 8px; }
</style>
</head>
<body>

<section class="card card-split" aria-label="Business card, split layout">
  <div class="panel"></div>
  <div class="brand">
    <div class="brand-name brand-name--red">BRIGHT OAK</div>
    <div class="tagline" style="color:var(--red)">More Than A Gym</div>
  </div>
  <ul class="contact contact--light">
    <li>2817 Mossgrove Bend Road</li>
    <li>Tavares, Florida 32190</li>
    <li>Phone: 352-555-Jump (5867)</li>
    <li>www.brightoakfitness.example</li>
    <li>info@brightoakfitness.example</li>
  </ul>
</section>

<section class="card card-slant" aria-label="Business card, diagonal layout">
  <svg class="card-bg" width="315" height="180" viewBox="0 0 315 180" aria-hidden="true">
    <polygon points="174,0 190,0 112,180 96,180" fill="var(--red)"/>
    <polygon points="186,0 315,0 315,180 108,180" fill="var(--black)"/>
  </svg>
  <div class="brand">
    <div class="brand-name brand-name--red" style="font-size:17px">BRIGHT OAK</div>
    <div class="tagline" style="color:var(--red);font-size:9.5px">More Than A Gym</div>
  </div>
  <ul class="contact contact--light">
    <li>2817 Mossgrove Bend Road</li>
    <li>Tavares, Florida 32190</li>
    <li style="height:17px"></li>
    <li>Phone: 352-555-Jump (5867)</li>
    <li>www.brightoakfitness.example</li>
    <li>info@brightoakfitness.example</li>
  </ul>
</section>

<section class="card card-bars" aria-label="Business card, bar layout">
  <svg class="card-bg" width="315" height="180" viewBox="0 0 315 180" aria-hidden="true">
    <rect x="0" y="0" width="315" height="12" fill="var(--red)"/>
    <rect x="0" y="158" width="150" height="22" fill="var(--red)"/>
    <polygon points="140,180 156,158 315,158 315,180" fill="var(--black)"/>
  </svg>
  <ul class="contact contact--dark">
    <li>2817 Mossgrove Bend Road</li>
    <li>Tavares, Florida 32190</li>
    <li class="gap"></li>
    <li><svg class="icon" viewBox="0 0 10 10" aria-hidden="true"><path d="M2 0.5 L4 2.8 L3 4 Q4.2 6 6 7 L7.2 6 L9.5 8 L8 9.6 Q3.5 9 0.4 2 Z"/></svg>352-555-Jump (5867)</li>
    <li><svg class="icon" viewBox="0 0 10 10" aria-hidden="true"><path d="M0 3.5 Q5 -1 10 3.5 L8.8 4.7 Q5 1.5 1.2 4.7 Z M2.2 5.8 Q5 3.4 7.8 5.8 L6.6 7 Q5 5.7 3.4 7 Z"/><circle cx="5" cy="8.6" r="1.2"/></svg>www.brightoakfitness.example</li>
    <li><svg class="icon" viewBox="0 0 10 10" aria-hidden="true"><rect x="0" y="1.5" width="10" height="7"/></svg>info@brightoakfitness.example</li>
  </ul>
  <div class="brand">
    <div class="brand-mark" style="background:var(--red)"></div>
    <div class="brand-name brand-name--red">BRIGHT OAK</div>
  </div>
  <div class="bar-tagline">More Than A Gym</div>
</section>

<section class="card card-header" aria-label="Business card, red header layout">
  <div class="top"></div>
  <div class="brand">
    <div class="brand-mark" style="background:var(--white)"></div>
    <div class="brand-name brand-name--white" style="font-size:21px">BRIGHT OAK</div>
  </div>
  <div class="band">More Than A Gym</div>
  <div class="contact contact--light">
    <div><span>2817 Mossgrove Bend Road</span><span>Tavares, Florida 32190</span></div>
    <div><span>Phone: 352-555-Jump (5867)</span><span>www.brightoakfitness.example</span></div>
    <div><span>info@brightoakfitness.example</span></div>
  </div>
</section>

</body>
</html>
```